Small Salsa business needs web design + coding

LA Brisa Verde is a small business started in Pocatello, Idaho and is looking to expand online. We focus on keeping the salsa all natural and more about savor than spiciness. Similar to the photo we've attached of just one of our salsas, we want a website that is friendly for users of all ages to use, as well as advertising in the website, and offer online shopping. Other things you think is beneficial to a small business like ours, proposals are welcomed and encouraged. We would also like to be able to remove and add stuff as we continue to grow our business.

Coding

```html
<!DOCTYPE html>
<html lang="en">
<head>
<meta charset="utf-8">
<title>LA Brisa Verde — All Natural Salsa</title>
<link href="https://fonts.googleapis.com/css2?family=Lora:wght@400;500;700&display=swap" rel="stylesheet">
<style>
  :root {
    --wood: #8b3a1a;
    --wood-dark: #6e2a12;
    --brand: #5a1f10;
    --ink: #1a1a1a;
    --muted: #6a6a6a;
    --cream: #f7f3ea;
    --footer: #1c1c1c;
    --white: #ffffff;
    --accent: #8e2a18;
  }
  * { box-sizing: border-box; margin: 0; padding: 0; }
  html, body { width: 1200px; height: 2804px; overflow: hidden; }
  body { font-family: "Lora", Georgia, serif; color: var(--ink); position: relative; background: var(--white); }
  a { color: inherit; text-decoration: none; }

  /* Hero */
  .hero {
    position: absolute; left: 0; top: 0; width: 1200px; height: 704px; overflow: hidden;
    background: linear-gradient(180deg, #8d3c1c 0%, #7f3317 45%, #8a391a 100%);
  }
  .brand-mark {
    position: absolute; left: 145px; top: 33px; width: 260px; height: 55px;
    background: var(--white); border-radius: 4px;
    display: flex; align-items: center; justify-content: center;
    font-weight: 700; font-size: 31px; color: var(--brand); letter-spacing: -0.5px;
  }
  .main-nav { position: absolute; top: 50px; left: 664px; display: flex; gap: 30px; }
  .main-nav a { color: var(--white); font-size: 14px; letter-spacing: 0.3px; padding-bottom: 8px; }
  .main-nav a.active { border-bottom: 3px solid var(--white); }
  .cart { position: absolute; left: 1004px; top: 44px; width: 40px; height: 34px; }
  .cart-badge {
    position: absolute; left: 1036px; top: 36px; width: 20px; height: 20px; border-radius: 50%;
    background: #111; color: var(--white); font-size: 11px; display: flex; align-items: center; justify-content: center;
  }
  .hero-title {
    position: absolute; top: 138px; left: 0; width: 1200px; text-align: center;
    color: var(--white); font-weight: 700; font-size: 104px; letter-spacing: -1px; line-height: 1.1;
  }
  .hero-tagline {
    position: absolute; top: 286px; left: 0; width: 1200px; text-align: center;
    color: var(--white); font-weight: 700; font-size: 19px;
  }
  .btn-outline-light {
    position: absolute; left: 514px; top: 356px; width: 173px; height: 65px;
    border: 2px solid var(--white); border-radius: 34px; color: var(--white);
    font-weight: 700; font-size: 18px; display: flex; align-items: center; justify-content: center;
  }
  .slider-dots { position: absolute; left: 1122px; top: 307px; display: flex; flex-direction: column; gap: 12px; }
  .slider-dots span { width: 8px; height: 8px; border-radius: 50%; background: var(--white); }
  .slider-dots span.current { background: transparent; border: 2px solid var(--white); }
  .hero-photo {
    position: absolute; left: 290px; top: 440px; width: 685px; height: 330px; border-radius: 50% 50% 0 0;
    background: radial-gradient(ellipse at 45% 45%, #f05a1e 0%, #d8481a 35%, #3a3431 70%, #2a2624 100%);
  }

  /* Content */
  .content {
    position: absolute; left: 0; top: 704px; width: 1200px; height: 1747px;
    background: linear-gradient(180deg, #ffffff 0%, #f8f5ee 30%, #fbf8f2 55%, #f6f1e5 100%);
  }
  .section-title { position: absolute; left: 0; width: 1200px; text-align: center; font-weight: 700; font-size: 50px; color: var(--ink); }
  .section-title em { font-style: normal; color: var(--brand); }
  .welcome-title { top: 82px; }
  .welcome-text {
    position: absolute; left: 196px; top: 168px; width: 808px; text-align: center;
    font-size: 12.6px; line-height: 27.3px; color: var(--muted);
  }
  .promo { position: absolute; top: 383px; height: 194px; overflow: hidden; }
  .promo-discount { left: 144px; width: 447px; background: #1f1f1f; }
  .promo-online { left: 607px; width: 448px; background: linear-gradient(135deg, #8a3a30 0%, #6f2c25 100%); }
  .promo-photo { position: absolute; top: 0; height: 194px; }
  .promo-discount .promo-photo { left: 0; width: 300px; background: radial-gradient(ellipse at 45% 55%, #c4381e 0%, #5d7a2a 35%, #242424 75%); }
  .promo-online .promo-photo { right: 0; width: 190px; background: radial-gradient(ellipse at 60% 50%, #e9d4a0 0%, #b8823d 40%, transparent 75%); }
  .promo-heading { position: absolute; font-weight: 700; font-size: 50px; line-height: 54px; color: var(--white); }
  .promo-discount .promo-heading { left: 318px; top: 24px; }
  .promo-discount .promo-heading .pct { color: #8e3420; }
  .promo-online .promo-heading { left: 43px; top: 24px; }
  .promo-link { position: absolute; top: 148px; font-size: 12px; color: var(--white); text-decoration: underline; }
  .promo-discount .promo-link { left: 318px; }
  .promo-online .promo-link { left: 43px; }
  .video {
    position: absolute; left: 144px; top: 593px; width: 912px; height: 439px;
    background: radial-gradient(ellipse at 52% 55%, #c9302a 0%, #a8351f 30%, #7a3a1c 55%, #3d2a1a 85%);
  }
  .play {
    position: absolute; left: 418px; top: 181px; width: 77px; height: 77px; border-radius: 50%; background: var(--white);
  }
  .feed-title { top: 1114px; }
  .feed-grid { position: absolute; left: 145px; top: 1222px; display: grid; grid-template-columns: repeat(4, 220px); grid-auto-rows: 168px; gap: 9px 10px; }
  .feed-tile { width: 220px; height: 168px; }
  .t1 { background: radial-gradient(circle at 45% 55%, #e8b52a 0%, #c6402a 35%, #2a2e35 75%); }
  .t2 { background: radial-gradient(circle at 65% 55%, #c43226 0%, #8c8c88 55%, #a3a29e 100%); }
  .t3 { background: radial-gradient(circle at 60% 40%, #7fa03a 0%, #e3c07a 45%, #8a7a66 100%); }
  .t4 { background: radial-gradient(circle at 45% 45%, #8cb83e 0%, #d6582a 45%, #4a3a2c 100%); }
  .t5 { background: radial-gradient(circle at 50% 60%, #e1522e 0%, #c94a2c 35%, #3a3a35 85%); }
  .t6 { background: linear-gradient(135deg, #5a3a2a 0%, #c9942e 40%, #a8342a 70%, #6a8a3a 100%); }
  .t7 { background: radial-gradient(circle at 50% 55%, #7a9a32 0%, #e07a2a 45%, #8a4c2a 100%); }
  .t8 { background: radial-gradient(circle at 60% 50%, #6a2a16 0%, #3c2c22 40%, #c9b07a 100%); }
  .btn-outline-dark {
    position: absolute; left: 514px; top: 1626px; width: 172px; height: 64px;
    border: 2px solid var(--brand); border-radius: 34px; color: var(--brand);
    font-weight: 700; font-size: 18px; display: flex; align-items: center; justify-content: center;
  }

  /* Footer */
  .site-footer { position: absolute; left: 0; top: 2451px; width: 1200px; height: 353px; background: var(--footer); color: var(--white); }
  .footer-heading { position: absolute; top: 68px; font-weight: 700; font-size: 20px; }
  .newsletter { position: absolute; left: 159px; top: 126px; width: 337px; height: 53px; border: 2px solid #555; border-radius: 28px; }
  .newsletter span { position: absolute; left: 32px; top: 17px; font-size: 12px; color: #ddd; }
  .newsletter .signup {
    position: absolute; right: 4px; top: 4px; width: 88px; height: 41px; border-radius: 22px; background: var(--accent);
    font-size: 13px; font-weight: 700; color: var(--white); display: flex; align-items: center; justify-content: center;
  }
  .quick-links { position: absolute; left: 573px; top: 119px; list-style: none; }
  .quick-links li { font-size: 14px; line-height: 26.5px; }
  .social { position: absolute; left: 797px; top: 124px; display: flex; gap: 42px; }
  .social span { width: 32px; height: 32px; border-radius: 50%; background: var(--white); }
  .payments { position: absolute; left: 797px; top: 190px; display: flex; gap: 8px; }
  .payments span { width: 32px; height: 22px; border-radius: 3px; background: #e8e3d6; }
  .copyright { position: absolute; left: 0; top: 287px; width: 1200px; text-align: center; font-size: 14px; }
</style>
</head>
<body>
  <header class="hero">
    <div class="brand-mark">LA Brisa Verde</div>
    <nav class="main-nav">
      <a href="#" class="active">HOME</a>
      <a href="#">SHOP</a>
      <a href="#">NEWS</a>
      <a href="#">CONTACT</a>
    </nav>
    <svg class="cart" viewBox="0 0 40 34" aria-label="Cart">
      <path d="M2 4 H9 L14 22 H33 L37 9 H11" fill="none" stroke="#fff" stroke-width="3.5" stroke-linejoin="round"/>
      <circle cx="16" cy="29" r="3" fill="#fff"/>
      <circle cx="31" cy="29" r="3" fill="#fff"/>
    </svg>
    <div class="cart-badge">0</div>
    <h1 class="hero-title">LA Brisa Verde</h1>
    <p class="hero-tagline">Lorem ipsum dolor sit amet consectetur adipiscing</p>
    <a href="#" class="btn-outline-light">SHOP NOW</a>
    <div class="slider-dots"><span></span><span></span><span class="current"></span><span></span><span></span></div>
    <div class="hero-photo" role="img" aria-label="Stone bowl filled with bright orange habanero peppers"></div>
  </header>

  <main class="content">
    <h2 class="section-title welcome-title">Welcome to <em>LA Brisa Verde</em></h2>
    <p class="welcome-text">Lorem ipsum dolor sit amet, consectetur adipiscing elit, sed do eiusmod tempor incididunt ut labore et dolore magna aliquis ipsum suspendisse ultrices gravida. Risus commodo viverra maecenas accumsan lacus vel facilisis. Lorem ipsum dolor sit ansectetdipiscing elit, sed do eiusmod tempor incididunt ut labore et dolore magis ipsum suspendisse ultrices gravida.us commodo viverra maecenas accumsan lacus vel facilisis. Lorem ipsum dolor sit amet, consectetur adipiscing do eiusmod tempor incididunt ut labore et dolore magna aliqua. Quis ipsum suspendisse ultrices gravida. Risus commodo viverra maecenas accumsan lacus vel facilisisorem ipsum dolor sit amet, consectetur adipiscing o eiusmod tempor incididunt ut labore et dolore magna aliquais ipsum</p>

    <section class="promo promo-discount">
      <div class="promo-photo" role="img" aria-label="Fresh salsa ingredients: tomatoes, cilantro, lime, chili and garlic"></div>
      <div class="promo-heading"><span class="pct">30%</span><br>OFF</div>
      <a href="#" class="promo-link">Shop Now</a>
    </section>
    <section class="promo promo-online">
      <div class="promo-photo" role="img" aria-label="Plate of tortilla chips with pico de gallo"></div>
      <div class="promo-heading">ONLINE<br>SHOPPING</div>
      <a href="#" class="promo-link">SHOP NOW</a>
    </section>

    <div class="video" role="img" aria-label="Video: clay bowl of fresh salsa with tortilla chips">
      <svg class="play" viewBox="0 0 77 77" aria-hidden="true">
        <circle cx="38.5" cy="38.5" r="38.5" fill="#fff"/>
        <path d="M29 22 L56 38.5 L29 55 Z" fill="#111" stroke="#111" stroke-width="4" stroke-linejoin="round"/>
      </svg>
    </div>

    <h2 class="section-title feed-title">Follow <em>Us SalsaFeed</em></h2>
    <div class="feed-grid">
      <div class="feed-tile t1" role="img" aria-label="Mango salsa in a wooden bowl"></div>
      <div class="feed-tile t2" role="img" aria-label="Salsa bowl with tomatoes and limes on stone"></div>
      <div class="feed-tile t3" role="img" aria-label="Chips with guacamole and red salsa"></div>
      <div class="feed-tile t4" role="img" aria-label="Guacamole with tomatoes and peppers"></div>
      <div class="feed-tile t5" role="img" aria-label="Glass bowl of tomato salsa with a chip"></div>
      <div class="feed-tile t6" role="img" aria-label="Rows of assorted salsas in small bowls"></div>
      <div class="feed-tile t7" role="img" aria-label="Pepper salsa surrounded by tortilla chips"></div>
      <div class="feed-tile t8" role="img" aria-label="Dark roasted salsa with crackers"></div>
    </div>
    <a href="#" class="btn-outline-dark">LOAD MORE</a>
  </main>

  <footer class="site-footer">
    <h3 class="footer-heading" style="left:159px">SIGN UP NEWSLETTER</h3>
    <div class="newsletter"><span>Enter Email</span><a href="#" class="signup">SIGN UP</a></div>
    <h3 class="footer-heading" style="left:573px">QUICK LINKS</h3>
    <ul class="quick-links">
      <li><a href="#">Home</a></li>
      <li><a href="#">Shop</a></li>
      <li><a href="#">News</a></li>
      <li><a href="#">Contact</a></li>
    </ul>
    <h3 class="footer-heading" style="left:797px">STAY CONNECTED</h3>
    <div class="social" aria-label="Social channels"><span></span><span></span><span></span><span></span></div>
    <div class="payments" aria-label="Accepted payment methods"><span></span><span></span><span></span><span></span><span></span></div>
    <p class="copyright">© 2021 LA Brisa Verde. All rights reserved &nbsp;|&nbsp; Privacy &nbsp;|&nbsp; Terms of Use</p>
  </footer>
</body>
</html>
```